Triple Pane Vanity Makeup Mirrors Packaging

We need a box design for a triple pane vanity we are selling for Corvid Bargains. Corvid logo is attached. There will need to be an area for a UPC code(code will be uploaded this week)

An Overview / Background of the Business & Services
-Corvid Bargains/Corvid Outlet is an online seller on the Brellix
marketplace(Canada and US). We sell a variety of products from
video games to home goods(fans, mirrors, lamps, oil diffusers, etc).

The Target Market / Audience you are trying to reach
-Mainly women who take their makeup preparation and application seriously.

Design Specifics; any preferences or ideas for Style, Colour, Imagery,
etc
-Please keep the design very feminine, classy, and professional.
- Include the company's logo on the design and use colors similar to
the logo(ie: red, orange, yellow) although tasteful use of other colors
will be considered.

Here are links to the products:

This mirror will be in white
https://www.tradevorn.example/product-detail/Tri-folding-fantastic-vanity-with-led_48190372615.html?spm=b3811.9552419.0.0.K28pt4

This mirror will be in black. It's dimensions are 32cm *20.5cm*10cm
https://www.tradevorn.example/product-detail/Customized-Tri-folding-make-up-led_2973048611.html?spm=b3811.9552419.0.0.K28pt4

The product description has been updated with links to the product.

Target Market(s)

Makeup and hair enthusiasts that want to take their preparation to the next level. These people use makeup and hair as an art, and the product will reflect that.

Industry/Entity Type

Hair And Beauty

Font styles to use
Decorative
Script

Colors

Designer to choose colors to be used in the design.

Requirements
Must have
• -Company logo
• -Spot for UPC code
Nice to have
• -this is our first packaging project and are very open to all ideas and designs.

```html
<!DOCTYPE html>
<html lang="en">
<head>
<meta charset="utf-8">
<title>Corvid Tri-Folding Makeup Mirror – Box Panels</title>
<link rel="stylesheet" href="https://fonts.googleapis.com/css2?family=Cinzel:wght@600;700;900&family=Open+Sans:wght@400;600;700&display=swap">
<style>
  :root {
    --bg: #e4e4e6;
    --paper: #f4f4f5;
    --damask: #e6e6e8;
    --red: #b8122a;
    --red-deep: #8a0a1c;
    --gold: #c9a04a;
    --gold-deep: #8e6a22;
    --ink: #1c1c1e;
    --text: #333336;
    --icon-line: #b8122a;
  }
  * { box-sizing: border-box; margin: 0; padding: 0; }
  html, body { width: 1200px; height: 1200px; overflow: hidden; background: var(--bg); }
  .canvas { position: relative; width: 1200px; height: 1200px; }

  .panel { position: absolute; overflow: hidden;
           background: linear-gradient(160deg, var(--paper), var(--damask)); }
  .panel--back { top: 30px; left: 90px; width: 1020px; height: 360px; }
  .panel--front { top: 420px; left: 90px; width: 620px; height: 750px; }
  .panel--side { top: 420px; left: 710px; width: 400px; height: 750px; border-left: 1px solid #cfcfd3; }

  .band { position: absolute; left: 0; top: 0; width: 100%; height: 100%; }

  .brand { position: absolute; display: flex; align-items: center; gap: 12px; }
  .brand__dot { border-radius: 50%; background: var(--red); }
  .brand__name { font-family: "Cinzel", serif; font-weight: 700; color: var(--red); }

  .title { position: absolute; font-family: "Cinzel", serif; font-weight: 900; line-height: 1.1; color: var(--ink); }
  .title__accent { color: var(--red); }

  /* Front panel */
  .panel--front .brand { top: 48px; left: 0; width: 100%; justify-content: center; }
  .panel--front .brand__dot { width: 20px; height: 20px; }
  .panel--front .brand__name { font-size: 42px; }
  .panel--front .title { top: 150px; left: 40px; width: 540px; }
  .panel--front .title__line1 { font-size: 44px; letter-spacing: 8px; }
  .panel--front .title__line2 { font-size: 44px; letter-spacing: 1px; }

  .seal { position: absolute; top: 30px; right: 26px; width: 104px; height: 104px; border-radius: 50%;
          background: radial-gradient(circle at 40% 35%, #f1d68e, var(--gold) 55%, var(--gold-deep));
          border: 3px solid #e9cf85; display: flex; flex-direction: column; align-items: center; justify-content: center;
          font-family: "Cinzel", serif; color: #3b2a08; }
  .seal__label { font-size: 8px; font-weight: 700; letter-spacing: 0.5px; }
  .seal__value { font-size: 26px; font-weight: 900; }

  .photo { position: absolute; top: 290px; left: 70px; width: 480px; height: 300px;
           background: linear-gradient(120deg, #d9a58f, #f2d2c2 45%, #c98a72); }
  .stand { position: absolute; top: 600px; left: 70px; width: 130px; height: 34px; border-radius: 50%;
           background: #fbfbfb; border: 2px solid #d8d8dc; }

  /* Side panel */
  .features { position: absolute; top: 60px; left: 0; width: 100%; padding: 0 30px;
              display: grid; grid-template-columns: 1fr 1fr; gap: 34px 20px; }
  .feature { display: flex; flex-direction: column; align-items: center; gap: 10px; }
  .feature__icon { width: 78px; height: 78px; border-radius: 50%; border: 3px solid var(--icon-line);
                   background: #fff; display: flex; align-items: center; justify-content: center; }
  .feature__label { font-family: "Open Sans", sans-serif; font-size: 15px; font-weight: 600; color: var(--text); }

  /* Back panel */
  .back__icons { position: absolute; top: 30px; left: 40px; display: flex; gap: 16px; }
  .back__icon { width: 48px; height: 48px; border-radius: 50%; border: 2px solid var(--icon-line);
                background: #fff; display: flex; align-items: center; justify-content: center; }
  .back__copy { position: absolute; top: 100px; left: 40px; width: 300px;
                font-family: "Open Sans", sans-serif; font-size: 14px; line-height: 1.5; color: var(--text); }
  .color-pick { position: absolute; top: 30px; left: 400px; font-family: "Open Sans", sans-serif; color: var(--text); }
  .color-pick__label { font-size: 17px; font-weight: 700; display: block; margin-bottom: 6px; }
  .color-pick__opts { display: flex; gap: 18px; font-size: 16px; align-items: center; }
  .color-pick__opt { display: flex; align-items: center; gap: 6px; }
  .swatch { width: 14px; height: 14px; border-radius: 50%; border: 1.5px solid var(--ink); }
  .swatch--on { background: var(--red); }
  .upc { position: absolute; top: 110px; left: 400px; width: 230px; height: 130px;
         background: #fff; border: 1px solid #cfcfd3; }
  .panel--back .brand { top: 40px; right: 50px; }
  .panel--back .brand__dot { width: 14px; height: 14px; }
  .panel--back .brand__name { font-size: 30px; }
  .panel--back .title { top: 110px; right: 50px; text-align: right; }
  .panel--back .title__line1 { font-size: 28px; letter-spacing: 5px; }
  .panel--back .title__line2 { font-size: 28px; }
</style>
</head>
<body>
<main class="canvas">

  <section class="panel panel--back" aria-label="Back panel">
    <svg class="band" viewBox="0 0 1020 360" aria-hidden="true">
      <path d="M0 250 C 200 250 400 290 620 300 C 800 310 920 280 1020 260 L1020 360 L0 360 Z" fill="#c9a04a"/>
      <path d="M0 258 C 200 258 400 298 620 308 C 800 318 920 288 1020 268 L1020 360 L0 360 Z" fill="var(--red)"/>
    </svg>

    <div class="back__icons">
      <div class="back__icon">
        <svg width="26" height="26" viewBox="0 0 44 44" fill="var(--icon-line)">
          <circle cx="10" cy="10" r="4"/><circle cx="22" cy="10" r="4"/><circle cx="34" cy="10" r="4"/>
          <circle cx="10" cy="22" r="4"/><circle cx="22" cy="22" r="4"/><circle cx="34" cy="22" r="4"/>
          <circle cx="10" cy="34" r="4"/><circle cx="22" cy="34" r="4"/><circle cx="34" cy="34" r="4"/>
        </svg>
      </div>
      <div class="back__icon">
        <svg width="26" height="26" viewBox="0 0 44 44" fill="none" stroke="var(--icon-line)" stroke-width="3">
          <rect x="14" y="8" width="16" height="30" rx="2"/><path d="M19 5 H25"/><path d="M18 28 H26"/>
        </svg>
      </div>
      <div class="back__icon">
        <svg width="26" height="26" viewBox="0 0 44 44" fill="none" stroke="var(--icon-line)" stroke-width="3">
          <path d="M10 34 L30 10"/><path d="M26 8 L34 16"/>
        </svg>
      </div>
    </div>

    <p class="back__copy">Bright LED light, two magnifying panes and a slim folding frame for flawless makeup at home or away.</p>

    <div class="color-pick">
      <span class="color-pick__label">Color:</span>
      <div class="color-pick__opts">
        <span class="color-pick__opt">white <span class="swatch swatch--on"></span></span>
        <span class="color-pick__opt">black <span class="swatch"></span></span>
      </div>
    </div>
    <div class="upc" aria-label="UPC code area"></div>

    <div class="brand">
      <span class="brand__dot"></span>
      <span class="brand__name">Corvid</span>
    </div>
    <h2 class="title">
      <div class="title__line1">TRI-FOLDING</div>
      <div class="title__line2"><span class="title__accent">MAKEUP</span> MIRROR</div>
    </h2>
  </section>

  <section class="panel panel--front" aria-label="Front panel">
    <svg class="band" viewBox="0 0 620 750" aria-hidden="true">
      <path d="M0 500 C 120 500 120 450 300 500 C 470 550 560 620 620 620 L620 750 L0 750 Z" fill="#c9a04a"/>
      <path d="M0 510 C 120 510 120 460 300 510 C 470 560 560 630 620 630 L620 750 L0 750 Z" fill="var(--red)"/>
      <path d="M0 690 L620 690 L620 750 L0 750 Z" fill="var(--red-deep)" opacity="0.35"/>
    </svg>

    <div class="brand">
      <span class="brand__dot"></span>
      <span class="brand__name">Corvid</span>
    </div>

    <div class="seal">
      <span class="seal__label">MAGNIFICATION</span>
      <span class="seal__value">2x3x</span>
    </div>

    <h1 class="title">
      <div class="title__line1">TRI-FOLDING</div>
      <div class="title__line2"><span class="title__accent">MAKEUP</span> MIRROR</div>
    </h1>

    <div class="photo" role="img" aria-label="Product photo: tri-folding lit makeup mirror reflecting a woman applying makeup"></div>
    <div class="stand"></div>
  </section>

  <section class="panel panel--side" aria-label="Side panel">
    <svg class="band" viewBox="0 0 400 750" aria-hidden="true">
      <path d="M0 630 C 140 630 260 590 400 550 L400 750 L0 750 Z" fill="#c9a04a"/>
      <path d="M0 640 C 140 640 260 600 400 560 L400 750 L0 750 Z" fill="var(--red)"/>
    </svg>

    <div class="features">
      <div class="feature">
        <div class="feature__icon">
          <svg width="44" height="44" viewBox="0 0 44 44" fill="var(--icon-line)">
            <circle cx="10" cy="10" r="4"/><circle cx="22" cy="10" r="4"/><circle cx="34" cy="10" r="4"/>
            <circle cx="10" cy="22" r="4"/><circle cx="22" cy="22" r="4"/><circle cx="34" cy="22" r="4"/>
            <circle cx="10" cy="34" r="4"/><circle cx="22" cy="34" r="4"/><circle cx="34" cy="34" r="4"/>
          </svg>
        </div>
        <span class="feature__label">12 LED lights</span>
      </div>
      <div class="feature">
        <div class="feature__icon">
          <svg width="44" height="44" viewBox="0 0 44 44" fill="none" stroke="var(--icon-line)" stroke-width="3">
            <circle cx="22" cy="22" r="14"/><path d="M22 12 V22"/>
          </svg>
        </div>
        <span class="feature__label">Touch switch</span>
      </div>
      <div class="feature">
        <div class="feature__icon">
          <svg width="44" height="44" viewBox="0 0 44 44" fill="none" stroke="var(--icon-line)" stroke-width="3">
            <rect x="14" y="8" width="16" height="30" rx="2"/><path d="M19 5 H25"/><path d="M18 28 H26"/>
          </svg>
        </div>
        <span class="feature__label">USB or battery</span>
      </div>
      <div class="feature">
        <div class="feature__icon">
          <svg width="44" height="44" viewBox="0 0 44 44" fill="none" stroke="var(--icon-line)" stroke-width="3">
            <path d="M10 34 L30 10"/><path d="M26 8 L34 16"/>
          </svg>
        </div>
        <span class="feature__label">Easy to clean</span>
      </div>
      <div class="feature">
        <div class="feature__icon">
          <svg width="44" height="44" viewBox="0 0 44 44" fill="none" stroke="var(--icon-line)" stroke-width="3">
            <path d="M34 22 A12 12 0 1 1 22 10"/><path d="M22 4 L28 10 L22 16"/>
          </svg>
        </div>
        <span class="feature__label">180° rotation</span>
      </div>
      <div class="feature">
        <div class="feature__icon">
          <svg width="44" height="44" viewBox="0 0 44 44" fill="none" stroke="var(--icon-line)" stroke-width="3">
            <rect x="10" y="8" width="24" height="28"/><path d="M22 8 V36"/>
          </svg>
        </div>
        <span class="feature__label">2x / 3x</span>
      </div>
    </div>
  </section>

</main>
</body>
</html>
```